Hospitality project presentation

I am developing a hospitality project and I need to present to the developer an outstanding presentation highlighting the overall look and feel. I will provide the text and most of the pictures (not all of them) some pictures (copyright free) will hae to be provided by the designer. Maximum number of pages 15, and zoom calls with me to make some adjustment if needed.

Industry/Entity Type

Hospitality

Font styles to use
Other font styles liked:
• calibri light

Requirements
Must have
• 15 slides
Nice to have
• Hospitality resort project look and feel

```html
<!DOCTYPE html>
<html lang="en">
<head>
<meta charset="utf-8">
<title>Hospitality Project Presentation</title>
<link rel="stylesheet" href="https://fonts.googleapis.com/css2?family=Carlito:wght@400;700&family=Open+Sans:wght@300;400&display=swap">
<style>
:root{
  --cyan:#00d4ef;
  --orange:#f7941d;
  --ink:#1e1e1e;
  --muted:#8a8a8a;
  --panel:#efefef;
  --white:#ffffff;
}
*{box-sizing:border-box;margin:0;padding:0}
html,body{width:1200px;height:2194px;overflow:hidden;background:var(--white)}
body{position:relative;font-family:"Carlito",Calibri,sans-serif;color:var(--ink)}
.slide{position:absolute;width:635px;height:357px;background:var(--white);overflow:hidden;transform:scale(.8517);transform-origin:0 0;box-shadow:14px 22px 40px rgba(0,0,0,.32)}
.abs{position:absolute}
.photo{position:absolute}
.brand{position:absolute;left:50px;top:24px;display:flex;align-items:center;gap:5px;font-size:8px;color:var(--orange);font-weight:700;white-space:nowrap}
.brand i{display:block;width:14px;height:14px;background:var(--orange)}
.dots{position:absolute;top:33px;right:44px;display:flex;gap:3px}
.dots b{width:5px;height:5px;border-radius:50%;background:#d9d9d9;display:block}
.dots b:nth-child(1){background:var(--orange)}
.dots b:nth-child(2){background:var(--cyan)}
.dots.on-cyan b{background:var(--white)}
.dots.on-cyan b:nth-child(1){background:var(--orange)}
.footer{position:absolute;left:48px;top:338px;font-size:6px;color:var(--muted)}
.rule{position:absolute;left:450px;top:341px;width:118px;height:1px;background:var(--cyan);opacity:.6}
.pgnum{position:absolute;left:583px;top:337px;font-size:6px;color:var(--muted)}
.title{position:absolute;font-family:"Open Sans",sans-serif;font-weight:300;color:var(--ink);line-height:1.15;white-space:nowrap}
.sub{position:absolute;font-family:"Open Sans",sans-serif;font-weight:300;color:var(--cyan);white-space:nowrap}
.para{position:absolute;font-size:6.4px;line-height:1.45;text-align:justify;color:var(--ink)}
.icon-box{position:absolute;width:52px;height:52px;border-radius:6px;background:var(--white);box-shadow:0 3px 10px rgba(0,0,0,.22);display:flex;align-items:center;justify-content:center}
.icon-box.accent{background:var(--cyan)}
.icon-box svg{width:30px;height:30px;fill:var(--ink)}
.icon-box.accent svg{fill:var(--white)}
.feat-title{position:absolute;font-size:11px;color:var(--cyan);white-space:nowrap}
.feat-text{position:absolute;font-size:6px;line-height:1.35;color:var(--ink)}
.col{position:absolute;width:96px;text-align:center}
.col .feat-t{font-size:10px;color:var(--cyan);margin-bottom:4px}
.col .feat-d{font-size:6px;line-height:1.35;text-align:justify}
</style>
</head>
<body>

<svg width="0" height="0" style="position:absolute" aria-hidden="true">
  <defs>
    <symbol id="i-cloche" viewBox="0 0 24 24"><path d="M2 17h20v2H2z M4 16a8 8 0 0 1 16 0z M11 6h2v2h-2z"/></symbol>
    <symbol id="i-chef" viewBox="0 0 24 24"><path d="M7 8a3 3 0 0 1 2-4 3 3 0 0 1 6 0 3 3 0 0 1 2 4v2H7z M8 11h8v3a4 4 0 0 1-8 0z M5 23v-3a5 5 0 0 1 5-4h4a5 5 0 0 1 5 4v3z"/></symbol>
    <symbol id="i-drink" viewBox="0 0 24 24"><path d="M3 9h9v12H3z M4 6h7v2H4z M14 3h7l-3 5v9h2v2h-6v-2h2V8z"/></symbol>
    <symbol id="i-pizza" viewBox="0 0 24 24"><path d="M12 2a10 10 0 1 0 0.01 0z M12 4.5a7.5 7.5 0 1 1-0.01 0z M11 5h2v14h-2z M5 11h14v2H5z"/><circle cx="8.5" cy="8.5" r="1.4"/><circle cx="15.5" cy="15.5" r="1.4"/><circle cx="15.5" cy="8.5" r="1.2"/></symbol>
    <symbol id="i-bed" viewBox="0 0 24 24"><path d="M1 6h2v8h19v5h-2v-3H3v3H1z M4 9h5v4H4z M10 10h11v3H10z"/></symbol>
    <symbol id="i-swim" viewBox="0 0 24 24"><circle cx="18" cy="8" r="2.3"/><path d="M3 14l6-5 4 1-3 3 5 2-3 1-4-2-3 2z M1 18c3-2 4 2 7 0s4 2 7 0 4 2 7 0v2c-3 2-4-2-7 0s-4-2-7 0-4-2-7 0z"/></symbol>
    <symbol id="i-snorkel" viewBox="0 0 24 24"><path d="M2 6h10v6H2z M4 8h6v2H4z M14 4h2v10a3 3 0 0 1-3 3h-2v-2h2a1 1 0 0 0 1-1z M1 19c3-2 4 2 7 0s4 2 7 0 4 2 7 0v2c-3 2-4-2-7 0s-4-2-7 0-4-2-7 0z"/></symbol>
    <symbol id="i-dive" viewBox="0 0 24 24"><circle cx="7" cy="5" r="2.3"/><path d="M4 9l3 1 6 6 7-10 2 1-8 12z M2 21h20v1.5H2z"/></symbol>
    <symbol id="i-paddle" viewBox="0 0 24 24"><path d="M2 14l18-10 1 1.8L3 15.8z M17 2l5 1-2 4-4-1z M1 18l4-4 2 2-4 4z M4 10c5 4 11 4 16 0l1 1.5c-6 5-12 5-18 0z"/></symbol>
    <symbol id="i-sail" viewBox="0 0 24 24"><path d="M12 2v15h8z M11 5L4 17h7z M2 18h20l-3 4H5z"/></symbol>
  </defs>
</svg>

<!-- Slide 1: Cover -->
<section class="slide cover" style="left:44px;top:106px">
  <div class="photo" role="img" aria-label="Beach shoreline with soft waves under a hazy sky" style="inset:0;background:linear-gradient(180deg,#cfe5ee 0%,#b9d6df 35%,#74c4cf 55%,#e8ded2 80%,#f2e9df 100%)"></div>
  <svg class="abs" style="left:0;top:0" width="635" height="357" viewBox="0 0 635 357" role="img" aria-label="Resort pool terrace with palm trees overlooking the sea">
    <defs>
      <linearGradient id="resort" x1="0" y1="0" x2="0" y2="1">
        <stop offset="0" stop-color="#6e9cb8"/>
        <stop offset=".35" stop-color="#1f6f96"/>
        <stop offset=".7" stop-color="#4f6a52"/>
        <stop offset="1" stop-color="#1a98b4"/>
      </linearGradient>
    </defs>
    <path d="M0 0H245C200 60 210 130 255 180C300 235 310 300 318 357H0Z" fill="url(#resort)"/>
  </svg>
  <div class="dots"><b></b><b></b><b></b><b></b></div>
  <div class="title" style="left:308px;top:136px;width:280px;text-align:center;font-size:34px;line-height:1.25;font-weight:400">Your Hospitality<br>Project title here</div>
  <div class="sub" style="left:308px;top:236px;width:280px;text-align:center;font-size:13px;font-weight:400">Your Hospitality subtitle Project goes here</div>
  <div class="abs" style="left:72px;top:288px;font-size:13px;color:var(--white)">CORALLINE RESORT</div>
</section>

<!-- Slide 2 -->
<section class="slide" style="left:615px;top:293px">
  <div class="abs" style="left:300px;top:0;width:335px;height:357px;background:var(--cyan)"></div>
  <div class="brand"><i></i>Coralline Resort</div>
  <div class="dots on-cyan"><b></b><b></b><b></b><b></b></div>
  <div class="photo" role="img" aria-label="Waiter arranging flowers on a set banquet table" style="left:0;top:82px;width:378px;height:194px;border:4px solid var(--white);border-left:0;background:linear-gradient(100deg,#d8c2a3 0%,#a67b4e 40%,#3b2a22 70%,#c9b49a 100%)"></div>
  <div class="title" style="left:412px;top:78px;font-size:26px;color:var(--white)">Your title slide</div>
  <div class="abs" style="left:412px;top:114px;font-size:10px;color:var(--white)">Lorem Ipsum is simply dummy text</div>
  <div class="icon-box" style="left:408px;top:150px"><svg><use href="#i-cloche"/></svg></div>
  <div class="feat-title" style="left:480px;top:151px;color:var(--white)">Your subtitle slide</div>
  <div class="feat-text" style="left:480px;top:167px;width:100px;color:var(--white)">Lorem Ipsum is simply dummy text of the printing and typesetting industry.</div>
  <div class="icon-box" style="left:408px;top:222px"><svg><use href="#i-chef"/></svg></div>
  <div class="feat-title" style="left:480px;top:223px;color:var(--white)">Your subtitle slide</div>
  <div class="feat-text" style="left:480px;top:239px;width:100px;color:var(--white)">Lorem Ipsum is simply dummy text of the printing and typesetting industry.</div>
  <div class="footer">Hospitality project name here</div>
  <div class="rule" style="background:var(--white)"></div>
  <div class="pgnum" style="color:var(--white)">2</div>
</section>

<!-- Slide 3 -->
<section class="slide" style="left:44px;top:480px">
  <div class="brand"><i></i>Coralline Resort</div>
  <div class="dots"><b></b><b></b><b></b><b></b></div>
  <svg class="abs" style="left:0;top:0" width="635" height="357" viewBox="0 0 635 357" role="img" aria-label="Restaurant dining room with a cyan tint">
    <path d="M0 240C120 200 200 225 330 240C450 255 540 250 635 260V357H0Z" fill="#33c6d8"/>
    <path d="M0 300C150 280 300 320 635 300V357H0Z" fill="#1fb3c7" opacity=".6"/>
  </svg>
  <div class="photo" role="img" aria-label="Waiter setting a dining table with flowers" style="left:77px;top:92px;width:190px;height:190px;border-radius:50%;border:4px solid var(--white);background:radial-gradient(circle at 60% 55%,#3b2b25,#a57c55 55%,#e0d2bd)"></div>
  <div class="photo" role="img" aria-label="Waiter carrying plated dishes" style="left:292px;top:196px;width:88px;height:88px;border-radius:50%;border:3px solid var(--white);background:radial-gradient(circle,#e7e2dc,#6b4b44 70%)"></div>
  <div class="photo" role="img" aria-label="Plated dessert on a dark table" style="left:405px;top:196px;width:88px;height:88px;border-radius:50%;border:3px solid var(--white);background:radial-gradient(circle,#e2b44c,#5c3a2a 70%)"></div>
  <div class="title" style="left:322px;top:66px;font-size:22px">Your title slide here</div>
  <div class="sub" style="left:322px;top:96px;font-size:12px">Lorem Ipsum simple dummy text</div>
  <div class="para" style="left:322px;top:118px;width:210px">Lorem Ipsum is simply dummy text of the printing and typesetting industry. Lorem Ipsum has been the industry's standard dummy text ever since the 1500s, when an unknown printer took a galley of type and scrambled it to make a type specimen book. It has survived not only five centuries, but also</div>
  <div class="footer" style="color:var(--white)">Hospitality project name here</div>
  <div class="rule" style="background:var(--white)"></div>
  <div class="pgnum" style="color:var(--white)">3</div>
</section>

<!-- Slide 4 -->
<section class="slide" style="left:615px;top:665px">
  <div class="brand"><i></i>Coralline Resort</div>
  <div class="dots"><b></b><b></b><b></b><b></b></div>
  <div class="title" style="left:65px;top:58px;font-size:25px;line-height:1.25">Your title<br>slide here</div>
  <div class="sub" style="left:65px;top:125px;font-size:11px">Lorem Ipsum dummy text</div>
  <div class="para" style="left:65px;top:148px;width:160px">Lorem Ipsum is simply dummy text of the printing and typesetting industry. Lorem Ipsum has been the industry's standard dummy text</div>
  <div class="icon-box accent" style="left:60px;top:206px;width:44px;height:44px"><svg style="width:24px;height:24px"><use href="#i-drink"/></svg></div>
  <div class="feat-title" style="left:123px;top:206px;font-size:10px">Your subtitle slide</div>
  <div class="feat-text" style="left:123px;top:222px;width:100px">Lorem Ipsum is simply dummy text of the printing and typesetting industry.</div>
  <div class="icon-box" style="left:60px;top:276px;width:44px;height:44px"><svg style="width:24px;height:24px"><use href="#i-pizza"/></svg></div>
  <div class="feat-title" style="left:125px;top:276px;font-size:10px">Your subtitle slide</div>
  <div class="feat-text" style="left:125px;top:292px;width:100px">Lorem Ipsum is simply dummy text of the printing and typesetting industry.</div>
  <div class="photo" role="img" aria-label="Slice of layered berry cake" style="left:301px;top:49px;width:144px;height:73px;background:linear-gradient(135deg,#5a4a4a,#f3dfe0 50%,#c9475a)"></div>
  <div class="photo" role="img" aria-label="Tacos with fresh salsa and lime" style="left:449px;top:49px;width:142px;height:202px;background:linear-gradient(160deg,#5b3a24,#d0772a 45%,#f0c35a 70%,#6e9a3a)"></div>
  <div class="photo" role="img" aria-label="Gourmet burger on a wooden board" style="left:301px;top:126px;width:144px;height:201px;background:linear-gradient(180deg,#7c7b79,#8b8682 30%,#d69a3a 55%,#6e3b20 85%,#4a2a18)"></div>
  <div class="photo" role="img" aria-label="Pizza slices on a board" style="left:449px;top:255px;width:142px;height:72px;background:linear-gradient(120deg,#c76a2c,#e8b46a 50%,#7a3b22)"></div>
  <div class="footer">Hospitality project name here</div>
  <div class="rule"></div>
  <div class="pgnum">4</div>
</section>

<!-- Slide 5 -->
<section class="slide" style="left:44px;top:852px">
  <div class="brand" style="left:36px"><i></i>Coralline Resort</div>
  <div class="dots"><b></b><b></b><b></b><b></b></div>
  <div class="abs" style="left:28px;top:57px;width:577px;height:137px;background:var(--panel)"></div>
  <div class="photo" role="img" aria-label="Sun loungers on a pool deck at sunset" style="left:43px;top:80px;width:143px;height:90px;background:linear-gradient(180deg,#c9d3d8,#e8d9bf 40%,#4c8ea0 60%,#6a4a33)"></div>
  <div class="photo" role="img" aria-label="Palm trees reflected in a pool" style="left:206px;top:80px;width:143px;height:90px;background:linear-gradient(180deg,#d8e4ea,#4b6e3a 45%,#8ec9d4 70%,#c3e1e8)"></div>
  <div class="photo" role="img" aria-label="Aerial view of a resort pool by the ocean" style="left:369px;top:80px;width:223px;height:90px;background:linear-gradient(180deg,#3b7ea6,#2c6a8f 30%,#4d7a4a 60%,#1fb0c2)"></div>
  <div class="title" style="left:0;top:214px;width:635px;text-align:center;font-size:17.5px;line-height:1.3;font-weight:400">Your extended title slide goes here, the space is interactive you<br><span style="color:var(--cyan)">could include all the text you need, the text shrink on overflow</span></div>
  <div class="para" style="left:50px;top:278px;width:535px;text-align:center;font-size:5.8px">Lorem Ipsum is simply dummy text of the printing and typesetting industry. Lorem Ipsum has been the industry's standard dummy text ever since the 1500s, when an unknown printer took a galley of type and scrambled it to make a type specimen book. It has survived not only five centuries, but also the leap into electronic typesetting, remaining essentially unchanged. It was popularized in the 1960s with the release of transfer sheets containing Lorem Ipsum passages, and more recently with desktop publishing software for page layouts including versions of Lorem Ipsum.</div>
  <div class="footer">Hospitality project name here</div>
  <div class="rule"></div>
  <div class="pgnum">5</div>
</section>

<!-- Slide 6 -->
<section class="slide" style="left:615px;top:1037px">
  <svg class="abs" style="left:0;top:0" width="635" height="357" viewBox="0 0 635 357" role="img" aria-label="Resort villa with lit infinity pool at dusk">
    <defs>
      <linearGradient id="dusk" x1="0" y1="0" x2="0" y2="1">
        <stop offset="0" stop-color="#2f62b8"/>
        <stop offset=".4" stop-color="#4c86d4"/>
        <stop offset=".6" stop-color="#1d3550"/>
        <stop offset=".8" stop-color="#1479b8"/>
        <stop offset="1" stop-color="#0b3c7a"/>
      </linearGradient>
    </defs>
    <path d="M400 0H635V357H320C330 280 380 250 395 190C410 130 385 60 400 0Z" fill="url(#dusk)"/>
  </svg>
  <div class="brand" style="left:36px"><i></i>Coralline Resort</div>
  <div class="dots on-cyan"><b></b><b></b><b></b><b></b></div>
  <div class="title" style="left:47px;top:66px;font-size:27px">Here your title slide</div>
  <div class="sub" style="left:47px;top:104px;font-size:14px">Lorem Ipsum is simply dummy text</div>
  <div class="icon-box accent" style="left:44px;top:155px"><svg><use href="#i-bed"/></svg></div>
  <div class="icon-box" style="left:113px;top:155px"><svg><use href="#i-drink"/></svg></div>
  <div class="icon-box" style="left:183px;top:155px"><svg><use href="#i-chef"/></svg></div>
  <div class="icon-box" style="left:252px;top:155px"><svg><use href="#i-swim"/></svg></div>
  <div class="para" style="left:44px;top:227px;width:270px">Lorem Ipsum is simply dummy text of the printing and typesetting industry. Lorem Ipsum has been the industry's standard dummy text ever since the 1500s, when an unknown printer took a galley of type and scrambled it to make a type specimen book. It has survived not only five centuries, but also the leap into electronic typesetting, remaining essentially unchanged. It was popularized in the 1960s with the release of transfer sheets containing Lorem Ipsum passages, and more recently with desktop publishing software for page layouts including</div>
  <div class="footer">Hospitality project name here</div>
</section>

<!-- Slide 7 -->
<section class="slide" style="left:44px;top:1224px">
  <div class="brand"><i></i>Coralline Resort</div>
  <div class="dots"><b></b><b></b><b></b><b></b></div>
  <div class="abs" style="left:30px;top:48px;width:280px;height:280px;border-radius:50%;background:var(--panel)"></div>
  <div class="photo" role="img" aria-label="Stack of pancakes with syrup being poured" style="left:55px;top:53px;width:194px;height:194px;border-radius:50%;background:radial-gradient(circle at 55% 60%,#e0a040,#8a5a2a 35%,#2f3438 65%)"></div>
  <div class="photo" role="img" aria-label="Plated seafood dish with sauce" style="left:150px;top:163px;width:150px;height:150px;border-radius:50%;border:4px solid var(--white);background:radial-gradient(circle at 45% 45%,#f0d9a8,#c9873c 45%,#3a3a34 80%)"></div>
  <div class="title" style="left:355px;top:112px;font-size:22px">Here your title slide</div>
  <div class="sub" style="left:355px;top:143px;font-size:11.5px">Lorem Ipsum is simply dummy text</div>
  <div class="para" style="left:355px;top:173px;width:225px">Lorem Ipsum is simply dummy text of the printing and typesetting industry. Lorem Ipsum has been the industry's standard dummy text ever since the 1500s, when an unknown printer took a galley of type and scrambled it to make a type specimen book. It has survived not only five centuries, but also the leap into electronic typesetting, remaining essentially unchanged. It was popularized in the 1960s with the release of transfer sheets containing Lorem Ipsum passages,</div>
  <div class="footer">Hospitality project name here</div>
  <div class="rule"></div>
  <div class="pgnum">7</div>
</section>

<!-- Slide 8 -->
<section class="slide" style="left:44px;top:1597px">
  <div class="brand"><i></i>Coralline Resort</div>
  <div class="dots"><b></b><b></b><b></b><b></b></div>
  <div class="title" style="left:0;top:14px;width:635px;text-align:center;font-size:23px">Here your title slide</div>
  <div class="sub" style="left:0;top:50px;width:635px;text-align:center;font-size:12px">Lorem Ipsum is simply dummy text</div>
  <div class="photo" role="img" aria-label="Tropical beach at sunset with gentle waves" style="left:0;top:83px;width:635px;height:130px;background:linear-gradient(180deg,#c9c7c4 0%,#e9c9a0 20%,#7fa7ad 40%,#2f9fa8 60%,#8fcfcf 80%,#e8e0d4 100%)"></div>
  <div class="icon-box accent" style="left:64px;top:185px"><svg><use href="#i-swim"/></svg></div>
  <div class="icon-box" style="left:176px;top:185px"><svg><use href="#i-snorkel"/></svg></div>
  <div class="icon-box" style="left:289px;top:185px"><svg><use href="#i-dive"/></svg></div>
  <div class="icon-box" style="left:401px;top:185px"><svg><use href="#i-paddle"/></svg></div>
  <div class="icon-box" style="left:514px;top:185px"><svg><use href="#i-sail"/></svg></div>
  <div class="col" style="left:42px;top:244px"><div class="feat-t">Your subtitle slide</div><div class="feat-d">Lorem Ipsum is simply dummy text of the printing and typesetting industry.</div></div>
  <div class="col" style="left:154px;top:244px"><div class="feat-t">Your subtitle slide</div><div class="feat-d">Lorem Ipsum is simply dummy text of the printing and typesetting industry.</div></div>
  <div class="col" style="left:267px;top:244px"><div class="feat-t">Your subtitle slide</div><div class="feat-d">Lorem Ipsum is simply dummy text of the printing and typesetting industry.</div></div>
  <div class="col" style="left:379px;top:244px"><div class="feat-t">Your subtitle slide</div><div class="feat-d">Lorem Ipsum is simply dummy text of the printing and typesetting industry.</div></div>
  <div class="col" style="left:492px;top:244px"><div class="feat-t">Your subtitle slide</div><div class="feat-d">Lorem Ipsum is simply dummy text of the printing and typesetting industry.</div></div>
  <div class="footer">Hospitality project name here</div>
  <div class="rule"></div>
  <div class="pgnum">8</div>
</section>

<!-- Slide 9 -->
<section class="slide" style="left:615px;top:1410px">
  <div class="brand"><i></i>Coralline Resort</div>
  <div class="dots"><b></b><b></b><b></b><b></b></div>
  <div class="abs" style="left:30px;top:72px;width:240px;height:258px;background:var(--panel)"></div>
  <div class="photo" role="img" aria-label="Wooden pool deck in warm light" style="left:43px;top:53px;width:153px;height:129px;background:linear-gradient(160deg,#c98a4a,#b06a2c 50%,#e0a864)"></div>
  <div class="abs" style="left:58px;top:78px;font-family:'Open Sans',sans-serif;font-weight:300;font-size:16px;line-height:1.4;color:var(--white)">Place Here<br>your dummy<br>subtitle slide</div>
  <div class="photo" role="img" aria-label="Palm trees around a resort pool" style="left:203px;top:53px;width:190px;height:129px;background:linear-gradient(180deg,#dce6ea,#4a6e3c 45%,#90c8d2 72%,#c6e2ea)"></div>
  <div class="photo" role="img" aria-label="Resort villa with lit pool at dusk" style="left:43px;top:188px;width:190px;height:129px;background:linear-gradient(180deg,#2f62b8,#4c86d4 40%,#1d3550 60%,#1479b8 85%,#0b3c7a)"></div>
  <div class="photo" role="img" aria-label="Aerial view of a pool beside the ocean" style="left:240px;top:188px;width:153px;height:129px;background:linear-gradient(180deg,#6ea2c4,#3a7aa0 30%,#567e4c 60%,#1fb0c2)"></div>
  <div class="title" style="left:425px;top:55px;font-size:22px;line-height:1.3">Place Here<br>your title slide</div>
  <div class="sub" style="left:425px;top:115px;font-size:12px;line-height:1.3">Lorem Ipsum is simply<br>dummy text</div>
  <div class="para" style="left:425px;top:180px;width:190px">Lorem Ipsum is simply dummy text of the printing and typesetting industry. Lorem Ipsum has been the industry's standard dummy text ever since the 1500s, when an unknown printer took a galley of type and scrambled it to make a type specimen book. It has survived not only five centuries, but also the leap into electronic typesetting, remaining essentially unchanged. It was popularized in the 1960s with the release of transfer sheets containing Lorem Ipsum passages, and more recently with desktop publishing software for page layouts including</div>
  <div class="footer">Hospitality project name here</div>
  <div class="rule"></div>
  <div class="pgnum">9</div>
</section>

<!-- Slide 10 -->
<section class="slide" style="left:615px;top:1783px">
  <div class="brand"><i></i>Coralline Resort</div>
  <div class="dots"><b></b><b></b><b></b><b></b></div>
  <div class="title" style="left:48px;top:68px;font-size:26px;line-height:1.25">Place Here<br>your title slide</div>
  <div class="sub" style="left:48px;top:138px;font-size:11px">Lorem Ipsum is simply dummy text</div>
  <div class="photo" role="img" aria-label="Sunset over a calm beach" style="left:270px;top:63px;width:173px;height:121px;background:linear-gradient(180deg,#c8ccd0,#f1cf9e 35%,#8fb8bb 55%,#e6d6c0)"></div>
  <div class="photo" role="img" aria-label="Aerial view of resort pool and ocean" style="left:455px;top:63px;width:137px;height:121px;background:linear-gradient(180deg,#3b7ea6,#2c6a8f 30%,#4d7a4a 60%,#1fb0c2)"></div>
  <div class="photo" role="img" aria-label="Palm-lined infinity pool" style="left:43px;top:194px;width:214px;height:121px;background:linear-gradient(180deg,#dce6ea,#4a6e3c 45%,#90c8d2 72%,#c6e2ea)"></div>
  <div class="photo" role="img" aria-label="Sun loungers on a deck at sunset" style="left:270px;top:194px;width:136px;height:121px;background:linear-gradient(180deg,#c9d3d8,#e8d9bf 40%,#4c8ea0 60%,#6a4a33)"></div>
  <div class="photo" role="img" aria-label="Resort villa with lit pool at night" style="left:418px;top:194px;width:174px;height:121px;background:linear-gradient(180deg,#2f62b8,#4c86d4 40%,#1d3550 60%,#1479b8 85%,#0b3c7a)"></div>
  <div class="footer">Hospitality project name here</div>
  <div class="rule"></div>
  <div class="pgnum">10</div>
</section>

</body>
</html>
```